Business Card design for Recruiter providing Recruitment Staff Augmentation services

I need a double sided business card. I have used Zek to print cards in the past and really like their quality. I have a logo but need to change the tagline that is part of the graphic.

The tagline currently reads and Connnecting people with careers - but it should be removed.

The back should look like a notecard for writing a to do list with the first to-do Augment Recruiting Staff

```html
<!DOCTYPE html>
<html lang="en">
<head>
<meta charset="UTF-8">
<title>To-Do Notecard – Card Back</title>
<link rel="stylesheet" href="https://fonts.googleapis.com/css2?family=Parisienne&display=swap">
<style>
  :root {
    --paper: #fcf9cf;
    --rule-blue: #5ea9f2;
    --margin-pink: #f0699b;
    --ink: #111111;
  }
  html, body {
    margin: 0;
    padding: 0;
    width: 1200px;
    height: 708px;
    overflow: hidden;
    background: var(--paper);
  }
  .notecard {
    position: relative;
    width: 1200px;
    height: 708px;
    background: var(--paper);
  }
  .notecard-rules {
    position: absolute;
    inset: 0;
    display: block;
  }
  .rule-line {
    stroke: var(--rule-blue);
    stroke-width: 2;
  }
  .margin-line {
    stroke: var(--margin-pink);
    stroke-width: 5;
  }
  .todo-item {
    font-family: "Parisienne", cursive;
    font-size: 54px;
    fill: var(--ink);
  }
</style>
</head>
<body>
  <main class="notecard">
    <svg class="notecard-rules" width="1200" height="708" viewBox="0 0 1200 708" xmlns="http://www.w3.org/2000/svg">
      <g class="ruled-lines">
        <line class="rule-line" x1="79" y1="1" x2="1200" y2="1"/>
        <line class="rule-line" x1="79" y1="44.5" x2="1200" y2="44.5"/>
        <line class="rule-line" x1="79" y1="89" x2="1200" y2="89"/>
        <line class="rule-line" x1="79" y1="133.5" x2="1200" y2="133.5"/>
        <line class="rule-line" x1="79" y1="178" x2="1200" y2="178"/>
        <line class="rule-line" x1="79" y1="222.5" x2="1200" y2="222.5"/>
        <line class="rule-line" x1="79" y1="267" x2="1200" y2="267"/>
        <line class="rule-line" x1="79" y1="311.5" x2="1200" y2="311.5"/>
        <line class="rule-line" x1="79" y1="356" x2="1200" y2="356"/>
        <line class="rule-line" x1="79" y1="400.5" x2="1200" y2="400.5"/>
        <line class="rule-line" x1="79" y1="445" x2="1200" y2="445"/>
        <line class="rule-line" x1="79" y1="489.5" x2="1200" y2="489.5"/>
        <line class="rule-line" x1="79" y1="534" x2="1200" y2="534"/>
        <line class="rule-line" x1="79" y1="578.5" x2="1200" y2="578.5"/>
        <line class="rule-line" x1="79" y1="623" x2="1200" y2="623"/>
        <line class="rule-line" x1="79" y1="667.5" x2="1200" y2="667.5"/>
      </g>
      <line class="margin-line" x1="77" y1="0" x2="77" y2="708"/>
      <text class="todo-item" x="84" y="131">Augment Recruiting Staff</text>
    </svg>
  </main>
</body>
</html>
```